Graphic Design for Company Van - White Marlo Pivot Haulmate 2019 LWB

We are a Electronic Security Systems Company specializing in CCTV, Intruder Alarms, Fire Alarms, Access Control and Gate Automation.
I am looking for a modern design for a van wrap to include company logo, phone number, website, the types of work we do (CCTV ect), and our QLR Licence number, its specifically for the model of van in the project name mentioned above. I will attach some of our branded signage and siren logo with some more details. thank you.

```html
<!DOCTYPE html>
<html lang="en">
<head>
<meta charset="utf-8">
<title>Rowan Secure – Van Wrap Layout</title>
<link href="https://fonts.googleapis.com/css2?family=Lato:wght@400;700;900&display=swap" rel="stylesheet">
<style>
  :root {
    --bg: #e8e9e8;
    --red: #e23a48;
    --red-light: #f0606a;
    --charcoal: #2b2b2d;
    --white: #ffffff;
    --ink: #1c1c1e;
    --steel-1: #f2f2f2;
    --steel-2: #9a9ca0;
    --glass: #5b5d61;
  }
  html, body {
    margin: 0;
    padding: 0;
    width: 1200px;
    height: 873px;
    overflow: hidden;
    background: var(--bg);
  }
  .canvas {
    position: relative;
    width: 1200px;
    height: 873px;
    font-family: "Lato", sans-serif;
  }
  .wrap-panel { position: absolute; display: block; overflow: visible; }
  .side-left { left: 60px; top: 160px; width: 630px; height: 254px; }
  .side-right { left: 60px; top: 453px; width: 630px; height: 254px; }
  .rear { left: 735px; top: 215px; width: 390px; height: 390px; }

  .brand-name { font-family: "Lato", sans-serif; font-weight: 700; fill: var(--ink); }
  .brand-tag { font-family: "Lato", sans-serif; font-weight: 400; fill: var(--ink); }
  .service-list { font-family: "Lato", sans-serif; font-weight: 700; fill: var(--white); font-size: 9.5px; }
  .phone { font-family: "Lato", sans-serif; font-weight: 400; fill: var(--red); }
  .phone-dark { font-family: "Lato", sans-serif; font-weight: 400; fill: var(--ink); }
  .web { font-family: "Lato", sans-serif; font-weight: 700; fill: var(--white); }
  .web-red { font-family: "Lato", sans-serif; font-weight: 700; fill: var(--red); }
  .licence { font-family: "Lato", sans-serif; fill: var(--white); }
</style>
</head>
<body>
<div class="canvas">

  <svg width="0" height="0" style="position:absolute" aria-hidden="true">
    <defs>
      <linearGradient id="steel" x1="0" y1="0" x2="1" y2="1">
        <stop offset="0" stop-color="var(--steel-1)"/>
        <stop offset="0.55" stop-color="var(--steel-2)"/>
        <stop offset="1" stop-color="#3a3b3e"/>
      </linearGradient>
      <linearGradient id="hall" x1="0" y1="0" x2="0" y2="1">
        <stop offset="0" stop-color="#c8495a"/>
        <stop offset="1" stop-color="#e9b6bf"/>
      </linearGradient>
      <clipPath id="side-body">
        <path d="M6 236 L6 196 Q4 162 16 142 Q34 128 82 120 L226 38 Q258 18 305 15 L582 13 Q604 15 608 40 L620 205 L614 236 Z"/>
      </clipPath>

      <g id="side-shapes">
        <g clip-path="url(#side-body)">
          <rect x="0" y="0" width="630" height="254" fill="var(--white)"/>
          <!-- red upper field -->
          <polygon points="0,141 630,82 630,0 0,0" fill="var(--red)"/>
          <!-- charcoal roof strip -->
          <polygon points="200,40 630,8 630,0 200,0" fill="var(--charcoal)"/>
          <!-- side glass -->
          <path d="M186 104 L236 52 L322 44 L324 112 L180 120 Z" fill="var(--glass)"/>
          <!-- charcoal lower band -->
          <polygon points="0,168 150,172 160,193 630,160 630,254 0,254" fill="var(--charcoal)"/>
          <!-- red accent near rear -->
          <polygon points="556,170 630,160 630,204 572,208" fill="var(--red)"/>
          <!-- camera photo area -->
          <path d="M446 24 Q470 12 612 12 L620 205 L520 205 Q480 190 470 150 Q440 110 446 24 Z" fill="url(#steel)" role="img" aria-label="Large photo of a bullet CCTV security camera"/>
        </g>
        <circle cx="112" cy="234" r="46" fill="var(--bg)"/>
        <circle cx="517" cy="236" r="46" fill="var(--bg)"/>
      </g>
    </defs>
  </svg>

  <!-- Left side of van -->
  <svg class="wrap-panel side-left" viewBox="0 0 630 254">
    <use href="#side-shapes"/>
    <g class="service-list" transform="rotate(-4 342 48)">
      <text x="342" y="48">• CCTV</text>
      <text x="343" y="60">• Intruder Alarms</text>
      <text x="344" y="72">• Fire Alarms</text>
      <text x="345" y="84">• Access Control and</text>
      <text x="352" y="96">Gate Automation</text>
    </g>
    <g class="service-icons" fill="none" stroke="var(--red)" stroke-width="1.4">
      <circle cx="84" cy="152" r="10"/>
      <rect x="78" y="149" width="11" height="6" fill="var(--red)" stroke="none"/>
      <circle cx="110" cy="150" r="10"/>
      <rect x="106" y="144" width="7" height="12"/>
      <circle cx="136" cy="148" r="10"/>
      <polygon points="130,145 134,145 139,141 139,155 134,151 130,151" fill="var(--red)" stroke="none"/>
      <circle cx="162" cy="146" r="10"/>
      <path d="M156 151 h12 v-3 q-6 -9 -12 0 Z" fill="var(--red)" stroke="none"/>
    </g>
    <rect x="186" y="124" width="54" height="54" fill="var(--red)" transform="rotate(-4 213 151)"/>
    <g transform="rotate(-4 271 149)">
      <text class="brand-name" x="250" y="149" font-size="31">Rowan Secure</text>
      <text class="brand-tag" x="252" y="168" font-size="12.5">CCTV &amp; Alarm Installation</text>
    </g>
    <text class="phone" x="178" y="212" font-size="15" transform="rotate(-4 178 212)">0818 555 014</text>
    <text class="web" x="284" y="204" font-size="16" transform="rotate(-4 284 204)">www.rowansecure.ie</text>
  </svg>

  <!-- Right side of van -->
  <svg class="wrap-panel side-right" viewBox="0 0 630 254">
    <use href="#side-shapes" transform="translate(630 0) scale(-1 1)"/>
    <g class="service-list" transform="rotate(3 203 44)">
      <text x="203" y="44">• CCTV</text>
      <text x="203" y="56">• Intruder Alarms</text>
      <text x="203" y="68">• Fire Alarms</text>
      <text x="203" y="80">• Access Control and</text>
      <text x="210" y="92">Gate Automation</text>
    </g>
    <g class="service-icons" fill="none" stroke="var(--red)" stroke-width="1.4">
      <circle cx="468" cy="145" r="10"/>
      <rect x="462" y="142" width="11" height="6" fill="var(--red)" stroke="none"/>
      <circle cx="494" cy="147" r="10"/>
      <rect x="490" y="141" width="7" height="12"/>
      <circle cx="520" cy="149" r="10"/>
      <polygon points="514,146 518,146 523,142 523,156 518,152 514,152" fill="var(--red)" stroke="none"/>
      <circle cx="546" cy="151" r="10"/>
      <path d="M540 156 h12 v-3 q-6 -9 -12 0 Z" fill="var(--red)" stroke="none"/>
    </g>
    <rect x="186" y="110" width="54" height="54" fill="var(--red)" transform="rotate(3 213 137)"/>
    <g transform="rotate(3 252 140)">
      <text class="brand-name" x="252" y="140" font-size="31">Rowan Secure</text>
      <text class="brand-tag" x="254" y="159" font-size="12.5">CCTV &amp; Alarm Installation</text>
    </g>
    <text class="phone" x="176" y="188" font-size="15" transform="rotate(3 176 188)">0818 555 014</text>
    <text class="web" x="282" y="200" font-size="16" transform="rotate(3 282 200)">www.rowansecure.ie</text>
  </svg>

  <!-- Rear doors -->
  <svg class="wrap-panel rear" viewBox="0 0 390 390">
    <defs>
      <clipPath id="rear-body">
        <path d="M20 40 Q20 10 50 8 L340 8 Q370 10 370 40 L370 300 L20 300 Z"/>
      </clipPath>
    </defs>
    <g clip-path="url(#rear-body)">
      <rect x="0" y="0" width="390" height="300" fill="var(--white)"/>
      <rect x="0" y="140" width="390" height="160" fill="url(#hall)" role="img" aria-label="Faded photo of a warehouse interior in red tones"/>
      <polygon points="150,300 390,250 390,300" fill="var(--charcoal)"/>
      <path d="M215 120 Q240 90 390 95 L390 250 L250 250 Q200 200 215 120 Z" fill="url(#steel)" role="img" aria-label="Large photo of a bullet CCTV security camera"/>
    </g>
    <rect x="80" y="236" width="66" height="40" rx="3" fill="#1a1a1a"/>
    <rect x="74" y="30" width="46" height="46" fill="var(--red)"/>
    <text class="brand-name" x="130" y="60" font-size="26">Rowan Secure</text>
    <text class="brand-tag" x="131" y="78" font-size="12">CCTV &amp; Alarm Installation</text>
    <text class="web-red" x="195" y="106" font-size="16" text-anchor="middle">www.rowansecure.ie</text>
    <text class="phone-dark" x="195" y="124" font-size="14" text-anchor="middle">0818 555 014</text>
    <circle cx="48" cy="175" r="6" fill="none" stroke="var(--white)" stroke-width="1.5"/>
    <text class="licence" x="60" y="171" font-size="5.5" font-weight="700">The Quality Licensing Registry</text>
    <text class="licence" x="60" y="178" font-size="5">An Clár Ceadúnas Slándála</text>
    <text class="licence" x="62" y="185" font-size="5" font-weight="700">QLR License No: 20573</text>
  </svg>

</div>
</body>
</html>
```